Ad design for a macarons brand

We are a dessert brand with one product line: macarons. Our products delight. Every bite is a dream!

We are launching a new product and would like to lunch a small tactical campaign for the product to boost sales.

The new macron is mango ganache and the middle a mix of sour mango and yuzu (https://www.plumvarell.com/about-the-fruit-584302).

Here are some images we took of the new macaron
https://www.fennlocker.com/sh/qrtwpzhkvbmls/AAFJtRWD-nxPlkhQZ7CeW4DLp?dl=0

I attach the brand guideline document.

Required sizes

1080 x 1350
1080 x 1920

```html
<!DOCTYPE html>
<html lang="en">
<head>
<meta charset="utf-8">
<title>Velora – Mango Yuzu Macaron Ad</title>
<link rel="stylesheet" href="https://fonts.googleapis.com/css2?family=Playfair+Display:wght@400;500&family=Outfit:wght@400&display=swap">
<style>
  :root {
    --mango: #f8b52f;
    --mango-light: #fbcb6b;
    --highlight: #fcd27c;
    --ink: #3e2f14;
    --stone: #a3a3a3;
    --photo-warm: #f2a93a;
    --photo-pale: #e9e3da;
    --logo-ink: #0b0b10;
  }
  * { margin: 0; padding: 0; box-sizing: border-box; }
  html, body { width: 960px; height: 1200px; overflow: hidden; }
  body { background: var(--stone); font-family: "Outfit", sans-serif; }
  .ad { position: relative; width: 960px; height: 1200px; overflow: hidden; }

  .hero-photo {
    position: absolute; left: 0; top: 0; width: 960px; height: 425px;
    background:
      radial-gradient(ellipse 60% 70% at 55% 45%, #f7b546 0%, transparent 70%),
      radial-gradient(ellipse 40% 60% at 10% 80%, var(--photo-pale) 0%, transparent 70%),
      linear-gradient(160deg, #f0c27a 0%, var(--photo-warm) 55%, #e79a2c 100%);
  }
  .accent-band {
    position: absolute; left: 0; top: 425px; width: 960px; height: 21px;
    background: var(--mango-light);
  }
  .copy-panel {
    position: absolute; left: 0; top: 446px; width: 960px; height: 508px;
    background: var(--mango);
  }
  .headline {
    position: absolute; left: 133px; top: 40px;
    font-family: "Playfair Display", serif; font-weight: 400;
    font-size: 72px; line-height: 85px; letter-spacing: -2.5px;
    color: var(--ink); text-transform: uppercase;
  }
  .body-copy {
    position: absolute; left: 133px; top: 216px; width: 480px;
    font-size: 36px; line-height: 58.5px; letter-spacing: -0.3px;
    color: var(--ink);
  }
  .body-copy .line {
    display: inline;
    background: linear-gradient(to bottom, transparent 55%, var(--highlight) 55%, var(--highlight) 92%, transparent 92%);
    padding-right: 8px;
  }
  .cta {
    position: absolute; left: 135px; top: 428px;
    display: flex; align-items: center; gap: 20px;
    font-family: "Playfair Display", serif; font-size: 25px; letter-spacing: -0.8px;
    color: var(--ink); text-decoration: none;
  }
  .cta span { text-decoration: underline; text-underline-offset: 5px; text-decoration-thickness: 1px; }

  .brand-footer {
    position: absolute; left: 0; top: 954px; width: 960px; height: 246px;
    background: var(--stone);
    display: flex; align-items: center; justify-content: center; gap: 16px;
  }
  .brand-mark { width: 22px; height: 22px; background: var(--logo-ink); }
  .brand-name {
    font-family: "Playfair Display", serif; font-weight: 500;
    font-size: 52px; letter-spacing: 1px; color: var(--logo-ink);
    text-transform: uppercase;
  }
</style>
</head>
<body>
  <main class="ad">
    <div class="hero-photo" role="img" aria-label="Close-up of mango yuzu macarons with golden shells and bright yellow filling, piled on white baking paper"></div>
    <div class="accent-band"></div>

    <section class="copy-panel">
      <h1 class="headline">Velora. Every<br>bite’s a dream.</h1>
      <p class="body-copy">
        <span class="line">For anyone seeking a</span><br>
        <span class="line">treat, a gift, or a lift, Velora</span><br>
        <span class="line">are the perfect product.</span>
      </p>
      <a class="cta" href="#">
        <span>TASTE THIS FLAVOR</span>
        <svg width="12" height="22" viewBox="0 0 12 22" aria-hidden="true">
          <polyline points="2,2 10,11 2,20" fill="none" stroke="#3e2f14" stroke-width="2"/>
        </svg>
      </a>
    </section>

    <footer class="brand-footer">
      <div class="brand-mark"></div>
      <div class="brand-name">Velora</div>
    </footer>
  </main>
</body>
</html>
```